New Business Card Design Project

Want a simple but attention grabbing business card. Back Side having mainly our logo and basic info-the front side a typical business card.

Contact Information for Business Card

Hearth & Basin Works
218 NW Larkfield Rd. Suite 207
Ankeny, Iowa 50021

phone- 515.284.7093

website is -hbwplains.com

```html
<!DOCTYPE html>
<html lang="en">
<head>
<meta charset="utf-8">
<title>Hearth &amp; Basin Works – Business Card</title>
<link rel="stylesheet" href="https://fonts.googleapis.com/css2?family=Arimo:wght@400;700&display=swap">
<style>
  :root {
    --backdrop: #e4e4e2;
    --card-navy: #0b1330;
    --card-navy-deep: #070c1f;
    --accent-orange: #e8622a;
    --accent-blue: #2c86d6;
    --text-light: #f2f3f6;
    --edge-orange: #c4471c;
  }
  * { box-sizing: border-box; margin: 0; padding: 0; }
  html, body {
    width: 1200px; height: 801px; overflow: hidden;
    background: var(--backdrop);
    font-family: "Arimo", Arial, sans-serif;
  }
  .sheet {
    width: 1200px; height: 801px;
    display: flex; align-items: center; justify-content: center; gap: 60px;
  }
  .card {
    width: 525px; height: 300px;
    background: radial-gradient(ellipse at 50% 40%, var(--card-navy) 0%, var(--card-navy-deep) 100%);
    border-bottom: 3px solid var(--edge-orange);
    color: var(--text-light);
    position: relative;
    box-shadow: 0 10px 24px rgba(0,0,0,.25);
  }
  /* Front */
  .card-front { padding: 34px 40px 26px; display: flex; flex-direction: column; align-items: center; }
  .brand-name {
    font-weight: 700; text-transform: uppercase; letter-spacing: 1px;
    color: var(--accent-blue);
    display: flex; align-items: center; gap: 10px;
  }
  .brand-name .brand-dot { width: 12px; height: 12px; border-radius: 50%; background: var(--accent-blue); }
  .card-front .brand-name { font-size: 27px; }
  .details { display: flex; align-items: center; margin-top: 34px; }
  .person { text-align: right; padding-right: 22px; }
  .person-name { color: var(--accent-orange); font-size: 20px; text-transform: uppercase; letter-spacing: .5px; }
  .person-role { font-size: 14px; margin-top: 6px; }
  .divider { width: 1px; height: 66px; background: var(--text-light); opacity: .8; }
  .contact-list { list-style: none; padding-left: 22px; font-size: 14px; }
  .contact-list li { display: flex; align-items: center; gap: 9px; line-height: 22px; }
  .contact-list svg { width: 13px; height: 13px; fill: var(--accent-orange); flex: none; }
  .contact-list .web-highlight { color: var(--accent-orange); }
  .address { margin-top: auto; font-size: 14px; letter-spacing: .2px; }
  /* Back */
  .card-back { display: flex; align-items: center; justify-content: center; }
  .card-back .brand-name { font-size: 30px; }
</style>
</head>
<body>
<main class="sheet">
  <section class="card card-front" aria-label="Business card front">
    <div class="brand-name"><span class="brand-dot"></span>Hearth &amp; Basin Works</div>
    <div class="details">
      <div class="person">
        <p class="person-name">Daniel Reeve</p>
        <p class="person-role">Manager</p>
      </div>
      <div class="divider"></div>
      <ul class="contact-list">
        <li>
          <svg viewBox="0 0 24 24" aria-hidden="true"><path d="M6.6 10.8a15 15 0 0 0 6.6 6.6l2.2-2.2a1 1 0 0 1 1-.25 11.4 11.4 0 0 0 3.6.57 1 1 0 0 1 1 1V20a1 1 0 0 1-1 1A17 17 0 0 1 3 4a1 1 0 0 1 1-1h3.5a1 1 0 0 1 1 1c0 1.25.2 2.45.57 3.57a1 1 0 0 1-.25 1z"/></svg>
          515.284.7093
        </li>
        <li>
          <svg viewBox="0 0 24 24" aria-hidden="true"><path d="M2 5h20v14H2z M2 5l10 8 10-8" stroke="#0b1330" stroke-width="1.5"/></svg>
          hello@hbwplains.com
        </li>
        <li>
          <svg viewBox="0 0 24 24" aria-hidden="true"><circle cx="12" cy="12" r="10"/><path d="M2 12h20M12 2c3 3 3 17 0 20M12 2c-3 3-3 17 0 20" stroke="#0b1330" stroke-width="1.5" fill="none"/></svg>
          <span>www.<span class="web-highlight">hbwplains</span>.com</span>
        </li>
      </ul>
    </div>
    <p class="address">218 NW Larkfield Rd. Suite 207, Ankeny, IA 50021</p>
  </section>

  <section class="card card-back" aria-label="Business card back">
    <div class="brand-name"><span class="brand-dot"></span>Hearth &amp; Basin Works</div>
  </section>
</main>
</body>
</html>
```